business cards, stationary, email signature
Professional
Greta Volsky
President
Corporate office:
3620 E Tamsin Road, Orange, CA 92814
Other locations in San Diego, CA and Reno, NV
greta@farwellgrp.net
www.farwellgrp.net
482650, K, D74
*8(a), *SDB, *SBE, *MBE, *DBE, *CBE
these certifications should be listed in the middle, bottom of the card.
■221119 – Other Electric Power Generation
■236210 – Industrial Building Construction
■236220 – Commercial and Institutional Building Construction
■237310 – Highway, Street, and Bridge Construction
■238160 – Roofing Contractors
■238170 – Siding Contractors
■238220 – Plumbing, Heating, and Air-Conditioning Contractors
■238310 – Drywall and Insulation Contractors
■238320 – Painting and Wall Covering Contractors
■238340 – Tile and Terrazzo Contractors
■238350 – Finish Carpentry Contractors
■238390 – Other Building Finishing Contractors
■238910 – Site Preparation Contractors
■238990 – All Other Specialty Trade Contractors
■541350 – Building Inspection Services
■561210 – Facilities Support Services
■561790 – Other Services to Buildings and Dwellings

```html
<!DOCTYPE html>
<html lang="en">
<head>
<meta charset="utf-8">
<title>Farwell Group — Stationery</title>
<link href="https://fonts.googleapis.com/css2?family=Open+Sans:wght@400;600;700&display=swap" rel="stylesheet">
<style>
  :root{
    --backdrop:#9b9c9e;
    --ink:#141414;
    --paper:#ffffff;
    --green:#7b8f2c;
    --blue:#2b9fd8;
    --muted:#6b6b6b;
    --rule:#c9c9c9;
    --mark:#e2b43a;
  }
  *{box-sizing:border-box;margin:0;padding:0}
  html,body{width:1200px;height:1037px;overflow:hidden;background:var(--backdrop)}
  body{font-family:"Open Sans",Arial,sans-serif;color:var(--ink)}
  .canvas{position:relative;width:1200px;height:1037px;overflow:hidden;background:var(--backdrop)}
  .piece{position:absolute;background:var(--paper);box-shadow:0 3px 10px rgba(0,0,0,.25);overflow:hidden}

  /* brand lockup */
  .brand{display:flex;align-items:center;gap:8px}
  .brand-dot{width:34px;height:34px;border-radius:50%;background:var(--mark);flex:none}
  .brand-name{font-weight:600;letter-spacing:.12em;text-transform:uppercase;color:var(--paper);font-size:15px}
  .brand.on-light .brand-name{color:var(--ink)}

  .wave{position:absolute;left:0;width:100%;display:block}

  /* business card front */
  .card{width:340px;height:195px}
  .card-front{background:var(--ink);color:var(--paper)}
  .card-front .brand{position:absolute;left:18px;top:16px}
  .card-person{position:absolute;left:18px;top:62px}
  .card-person .name{font-size:13px;font-weight:700}
  .card-person .title{font-size:9px;color:#c8c8c8;margin-bottom:6px}
  .card-person p{font-size:8px;line-height:1.45;color:#e6e6e6}
  .card-certs{position:absolute;left:0;right:0;bottom:10px;text-align:center;font-size:8px;font-weight:600;letter-spacing:.05em;color:var(--ink);z-index:2}

  /* business card back */
  .card-back .brand{position:absolute;right:14px;top:10px}
  .card-back .brand-dot{width:20px;height:20px}
  .card-back .brand-name{font-size:10px}
  .naics{position:absolute;left:14px;top:38px;right:14px;columns:2;column-gap:10px;list-style:none}
  .naics li{font-size:5.6px;line-height:1.55;white-space:nowrap;overflow:hidden;text-overflow:ellipsis}
  .naics li::before{content:"";display:inline-block;width:4px;height:4px;background:var(--blue);margin-right:3px;vertical-align:middle}

  /* sheets */
  .sheet{width:370px;height:479px}
  .sheet-head{position:absolute;left:0;top:0;width:100%;height:96px}
  .sheet .brand{position:absolute;left:22px;top:20px;z-index:2}
  .sheet-contact{position:absolute;right:20px;top:14px;text-align:right;font-size:7px;line-height:1.5;color:#e6e6e6;z-index:2}
  .watermark{position:absolute;left:110px;top:170px;width:150px;height:150px;border-radius:50%;background:var(--mark);opacity:.12}

  .fax-title{position:absolute;left:28px;top:120px;font-size:20px;font-weight:700;letter-spacing:.08em}
  .fax-fields{position:absolute;left:28px;right:28px;top:160px;display:grid;grid-template-columns:1fr 1fr;column-gap:18px;row-gap:14px}
  .fax-field{display:flex;gap:6px;align-items:flex-end;font-size:8px;font-weight:600}
  .fax-field span.line{flex:1;border-bottom:1px solid var(--rule);height:10px}
  .fax-checks{position:absolute;left:28px;right:28px;top:268px;display:flex;justify-content:space-between;font-size:7.5px}
  .fax-checks span::before{content:"";display:inline-block;width:7px;height:7px;border:1px solid var(--ink);margin-right:4px;vertical-align:-1px}

  /* envelope */
  .envelope{width:660px;height:290px}
  .envelope .brand{position:absolute;left:26px;top:24px;z-index:2}
  .envelope-return{position:absolute;left:26px;top:70px;font-size:8px;line-height:1.5;color:#e6e6e6;z-index:2}
</style>
</head>
<body>
<svg width="0" height="0" style="position:absolute" aria-hidden="true">
  <defs>
    <symbol id="head-wave" viewBox="0 0 400 100" preserveAspectRatio="none">
      <path d="M0,0H400V50C280,86 140,92 0,66Z" fill="#141414"/>
      <path d="M0,72C140,98 280,92 400,56" fill="none" stroke="#2b9fd8" stroke-width="3"/>
      <path d="M0,80C140,106 280,100 400,64" fill="none" stroke="#7b8f2c" stroke-width="3"/>
    </symbol>
    <symbol id="foot-wave" viewBox="0 0 400 60" preserveAspectRatio="none">
      <path d="M0,38C130,8 270,10 400,28V60H0Z" fill="#7b8f2c"/>
      <path d="M0,44C130,16 270,18 400,36V60H0Z" fill="#ffffff"/>
      <path d="M0,50C130,24 270,26 400,42" fill="none" stroke="#2b9fd8" stroke-width="4"/>
    </symbol>
    <symbol id="card-wave" viewBox="0 0 400 60" preserveAspectRatio="none">
      <path d="M0,30C130,0 270,4 400,22V60H0Z" fill="#2b9fd8"/>
      <path d="M0,36C130,8 270,12 400,30V60H0Z" fill="#ffffff"/>
      <path d="M220,60C300,40 360,36 400,38V60Z" fill="#7b8f2c"/>
    </symbol>
  </defs>
</svg>

<main class="canvas">

  <!-- letterhead -->
  <section class="piece sheet letterhead" style="left:40px;top:40px">
    <svg class="sheet-head" aria-hidden="true"><use href="#head-wave"/></svg>
    <div class="brand"><span class="brand-dot"></span><span class="brand-name">Farwell Group</span></div>
    <div class="sheet-contact">3620 E Tamsin Road<br>Orange, CA 92814<br>greta@farwellgrp.net<br>www.farwellgrp.net</div>
    <div class="watermark"></div>
    <svg class="wave" style="bottom:0;height:44px" aria-hidden="true"><use href="#foot-wave"/></svg>
  </section>

  <!-- fax cover -->
  <section class="piece sheet fax" style="left:430px;top:40px">
    <svg class="sheet-head" aria-hidden="true"><use href="#head-wave"/></svg>
    <div class="brand"><span class="brand-dot"></span><span class="brand-name">Farwell Group</span></div>
    <div class="sheet-contact">3620 E Tamsin Road<br>Orange, CA 92814<br>Phone (714) 555-0142<br>Fax (714) 555-0143</div>
    <h1 class="fax-title">FAX</h1>
    <div class="fax-fields">
      <div class="fax-field">To:<span class="line"></span></div>
      <div class="fax-field">From:<span class="line"></span></div>
      <div class="fax-field">Fax:<span class="line"></span></div>
      <div class="fax-field">Pages:<span class="line"></span></div>
      <div class="fax-field">Phone:<span class="line"></span></div>
      <div class="fax-field">Date:<span class="line"></span></div>
      <div class="fax-field">Re:<span class="line"></span></div>
      <div class="fax-field">CC:<span class="line"></span></div>
    </div>
    <div class="fax-checks">
      <span>Urgent</span><span>For Review</span><span>Please Comment</span><span>Please Reply</span>
    </div>
    <svg class="wave" style="bottom:0;height:44px" aria-hidden="true"><use href="#foot-wave"/></svg>
  </section>

  <!-- business card front -->
  <section class="piece card card-front" style="left:830px;top:40px">
    <div class="brand"><span class="brand-dot"></span><span class="brand-name">Farwell Group</span></div>
    <div class="card-person">
      <div class="name">Greta Volsky</div>
      <div class="title">President</div>
      <p>Corporate office: 3620 E Tamsin Road, Orange, CA 92814</p>
      <p>Other locations in San Diego, CA and Reno, NV</p>
      <p>greta@farwellgrp.net · www.farwellgrp.net</p>
      <p>482650, K, D74</p>
    </div>
    <svg class="wave" style="bottom:0;height:38px" aria-hidden="true"><use href="#card-wave"/></svg>
    <div class="card-certs">*8(a) · *SDB · *SBE · *MBE · *DBE · *CBE</div>
  </section>

  <!-- business card back -->
  <section class="piece card card-back" style="left:830px;top:260px">
    <div class="brand on-light"><span class="brand-dot"></span><span class="brand-name">Farwell Group</span></div>
    <ul class="naics">
      <li>221119 – Other Electric Power Generation</li>
      <li>236210 – Industrial Building Construction</li>
      <li>236220 – Commercial and Institutional Building Construction</li>
      <li>237310 – Highway, Street, and Bridge Construction</li>
      <li>238160 – Roofing Contractors</li>
      <li>238170 – Siding Contractors</li>
      <li>238220 – Plumbing, Heating, and Air-Conditioning Contractors</li>
      <li>238310 – Drywall and Insulation Contractors</li>
      <li>238320 – Painting and Wall Covering Contractors</li>
      <li>238340 – Tile and Terrazzo Contractors</li>
      <li>238350 – Finish Carpentry Contractors</li>
      <li>238390 – Other Building Finishing Contractors</li>
      <li>238910 – Site Preparation Contractors</li>
      <li>238990 – All Other Specialty Trade Contractors</li>
      <li>541350 – Building Inspection Services</li>
      <li>561210 – Facilities Support Services</li>
      <li>561790 – Other Services to Buildings and Dwellings</li>
    </ul>
  </section>

  <!-- envelope -->
  <section class="piece envelope" style="left:40px;top:570px">
    <svg class="wave" style="top:0;height:130px;width:60%" aria-hidden="true"><use href="#head-wave"/></svg>
    <div class="brand"><span class="brand-dot"></span><span class="brand-name">Farwell Group</span></div>
    <div class="envelope-return">3620 E Tamsin Road<br>Orange, CA 92814</div>
    <svg class="wave" style="bottom:0;height:50px" aria-hidden="true"><use href="#foot-wave"/></svg>
  </section>

  <!-- second business card front -->
  <section class="piece card card-front" style="left:830px;top:570px">
    <div class="brand"><span class="brand-dot"></span><span class="brand-name">Farwell Group</span></div>
    <div class="card-person">
      <div class="name">Greta Volsky</div>
      <div class="title">President</div>
      <p>Corporate office: 3620 E Tamsin Road, Orange, CA 92814</p>
      <p>Other locations in San Diego, CA and Reno, NV</p>
      <p>greta@farwellgrp.net · www.farwellgrp.net</p>
      <p>482650, K, D74</p>
    </div>
    <svg class="wave" style="bottom:0;height:38px" aria-hidden="true"><use href="#card-wave"/></svg>
    <div class="card-certs">*8(a) · *SDB · *SBE · *MBE · *DBE · *CBE</div>
  </section>

</main>
</body>
</html>
```